Core Values Banner For Hearthwell Partners Inc

We want to take the core values for our small growing chimney service company and post them for our entire team to see on a daily basis. We want to be remind everyone how important this is too us all. IntegrityWe try to be honest and accountable in all aspects of our business, as well as in our personal interactions. We do what we say we will do, when we say we will do it, and how we say we will do it.Kaizen“Change for the best”We strive to constantly grow and improve, both personally and professionally. We own up to our mistakes and strive to resolve and learn from them. We actively seek feedback from our clients and each other. We believe the most innovative ideas come when we intentionally look for them.FamilyWe are a family-owned business, and we consider everyone who works here and every one we serve to be part of the family. Being honest and genuine with each other and our customers is what sets us apart. We put ourselves in our customer’s shoes and make recommendations as if it were our chimney, our home and our family.

Font styles to use
Serif
Sans Serif

Colors
ec1f27

Requirements
Must have
• This banner will be approximately 2.5' in height and 6 to 6.5' in width.
• I would like all 3 core values and there definitions listed on the banner
• check out the feel of our marketing on our website www.hearthwellpartnersvt.example

```html
<!DOCTYPE html>
<html lang="en">
<head>
<meta charset="utf-8">
<title>Hearthwell Partners Inc — Core Values</title>
<link rel="stylesheet" href="https://fonts.googleapis.com/css2?family=Share+Tech+Mono&family=VT323&display=swap">
<style>
  :root {
    --brand-red: #ec1f27;
    --deep-red: #8a0e12;
    --heading-ink: #4a0a0c;
    --paper: #ffffff;
    --text-light: #ffffff;
  }
  * { margin: 0; padding: 0; box-sizing: border-box; }
  html, body { width: 1200px; height: 462px; overflow: hidden; background: var(--paper); }
  .banner { position: relative; width: 1200px; height: 462px; background: var(--paper); }

  .band { position: absolute; background: var(--brand-red); }
  .value-title {
    position: absolute;
    font-family: "VT323", monospace;
    color: var(--heading-ink);
    font-size: 40px;
    letter-spacing: 2px;
    line-height: 1;
  }
  .value-tagline {
    position: absolute;
    font-family: "Share Tech Mono", monospace;
    color: var(--text-light);
    font-size: 13px;
  }
  .value-list {
    position: absolute;
    list-style: none;
    font-family: "Share Tech Mono", monospace;
    color: var(--text-light);
    font-size: 17px;
    line-height: 1.12;
  }
  .value-list li { position: relative; padding-left: 20px; margin-bottom: 10px; }
  .value-list li::before {
    content: ""; position: absolute; left: 0; top: 6px;
    width: 8px; height: 8px; background: var(--text-light);
  }
  .value-list.tight li { margin-bottom: 5px; }
  .accent { color: var(--deep-red); }
</style>
</head>
<body>
<main class="banner">
  <!-- Integrity row -->
  <div class="band" style="left:0;top:5px;width:1067px;height:141px"></div>
  <div class="band" style="left:1083px;top:5px;width:58px;height:141px"></div>
  <div class="band" style="left:1156px;top:5px;width:36px;height:141px"></div>
  <h2 class="value-title" style="left:10px;top:60px">INTEGRITY</h2>
  <ul class="value-list" style="left:195px;top:10px;width:860px">
    <li>We try to be <span class="accent">honest</span> and accountable in all aspects of our business, as well as in our personal interactions</li>
    <li style="margin-top:22px">We do what we say we will do, when we say we will do it, and how we say we will do it .</li>
  </ul>

  <!-- Kaizen row -->
  <div class="band" style="left:0;top:161px;width:97px;height:145px"></div>
  <div class="band" style="left:112px;top:161px;width:1076px;height:145px"></div>
  <h2 class="value-title" style="left:142px;top:194px">KAIZEN</h2>
  <p class="value-tagline" style="left:122px;top:234px">„Change for the best"</p>
  <ul class="value-list tight" style="left:295px;top:168px;width:880px">
    <li>We strive to constantly <span class="accent">grow</span> and improve, both personally and professionally.</li>
    <li>We own up to our mistakes and strive to resolve and learn from them.</li>
    <li>We actively seek feedback from our clients and each other.</li>
    <li>We believe the most <span class="accent">innovative ideas</span> come when we intentionally look for them.</li>
  </ul>

  <!-- Family row -->
  <div class="band" style="left:0;top:317px;width:1067px;height:138px"></div>
  <div class="band" style="left:1083px;top:317px;width:58px;height:138px"></div>
  <div class="band" style="left:1156px;top:317px;width:36px;height:138px"></div>
  <h2 class="value-title" style="left:14px;top:370px">FAMILY</h2>
  <ul class="value-list tight" style="left:132px;top:322px;width:925px">
    <li>We are a <span class="accent">family-owned business</span>, and we consider everyone who works here and every one we serve to be part of the family.</li>
    <li>Being honest and genuine with each other and our customers is what sets us apart.</li>
    <li>We put ourselves in our customer's shoes and make recommendations as if it were our chimney, our home and our family.</li>
  </ul>
</main>
</body>
</html>
```